Escrow Accounting firm needs a website design for a startup that services clients nationally.

I offer escrow accounting services for title companies and real estate attorneys. I've enclosed a logo, color palette and flyers with content that can be used for the site.

I'm looking for a similar design concept as the website below from my former employer. Please don't copy because of copyright infringement. Including for design ideas only.
www.harborlinefiduciary.com

Below is a brief write-up...
For professionals in the title insurance industry, finding a trustworthy and budget-friendly solution for escrow accounting can be daunting. When choosing the right accounting partner, title companies and law firms need a group they can rely on, and that's where we come in.

```html
<!DOCTYPE html>
<html lang="en">
<head>
<meta charset="utf-8">
<title>Meridian Escrow Solutions</title>
<link href="https://fonts.googleapis.com/css2?family=Montserrat:ital,wght@0,400;0,500;0,600;0,700;0,800;0,900;1,800;1,900&family=Roboto:wght@300;400;500;700&display=swap" rel="stylesheet">
<style>
:root{
  --copper:#c0725a;
  --copper-dark:#a95f49;
  --navy:#363e4e;
  --navy-deep:#1f2a38;
  --ink:#2d3340;
  --text:#3a3a3a;
  --muted:#555b66;
  --blush:#f7ecea;
  --blush-line:#d9b3a7;
  --white:#ffffff;
}
*{box-sizing:border-box;margin:0;padding:0}
html,body{width:1200px;height:3720px;overflow:hidden}
body{position:relative;background:var(--white);font-family:'Roboto',sans-serif;color:var(--text)}
.abs{position:absolute}
.heading{font-family:'Montserrat',sans-serif;font-weight:900;color:var(--ink);text-transform:uppercase;letter-spacing:.5px}
.accent{color:var(--copper)}
.eyebrow{font-family:'Montserrat',sans-serif;font-weight:700;color:var(--copper);text-transform:uppercase;letter-spacing:1px}
.divider{position:absolute;height:14px}
.divider::before,.divider::after{content:"";position:absolute;top:7px;height:1px;background:var(--copper);width:calc(50% - 16px)}
.divider::before{left:0}.divider::after{right:0}
.divider span{position:absolute;left:50%;top:0;width:14px;height:14px;margin-left:-7px;border:1.5px solid var(--copper);border-radius:50%}
.brand{display:flex;align-items:center;gap:12px;font-family:'Montserrat',sans-serif;font-weight:500;color:var(--white);font-size:30px;line-height:1;letter-spacing:1px;text-transform:uppercase}
.brand-mark{width:40px;height:40px;border-radius:50%;background:var(--copper)}
.btn{position:absolute;display:flex;align-items:center;justify-content:center;gap:8px;font-family:'Montserrat',sans-serif;font-weight:700;font-size:12px;color:var(--white);background:var(--copper);border-radius:0 20px 0 20px}
.btn svg{width:16px;height:8px}

/* hero */
.hero{left:0;top:0;width:1200px;height:664px;border-bottom-right-radius:170px;overflow:hidden;
  background:linear-gradient(100deg,#16212d 0%,#213142 38%,#3a5468 62%,#6d8597 82%,#8ea2b1 100%);
  box-shadow:inset -4px -4px 0 var(--copper)}
.hero-topbar{left:744px;top:16px;font-size:11px;color:var(--white);display:flex;gap:14px}
.hero-topbar svg{width:11px;height:11px;vertical-align:-1px;margin-right:5px;fill:var(--white)}
.nav{top:56px;font-size:12px;color:var(--white)}
.hero-eyebrow{left:113px;top:205px;font-size:13px}
.hero-title{left:113px;top:244px;font-size:38px;line-height:37px;color:var(--white)}
.hero-copy{left:113px;top:372px;width:320px;font-size:12px;line-height:16px;color:#e3e7ec}
.dots{left:113px;top:536px;display:flex;align-items:center;gap:17px}
.dots .ring{width:34px;height:34px;border:1.5px solid var(--copper);border-radius:50%;display:flex;align-items:center;justify-content:center}
.dots .ring::after{content:"";width:4px;height:4px;background:var(--white);border-radius:50%}
.dots i{width:5px;height:5px;border-radius:50%;background:var(--white);display:block}

/* about */
.about-photo{left:113px;top:765px;width:476px;height:506px;background:linear-gradient(160deg,#e9e4e2 0%,#c7aca1 40%,#4a5466 100%);border-radius:16px}
.about-eyebrow{left:654px;top:768px;font-size:9px}
.about-title{left:654px;top:800px;font-size:29px;line-height:29px}
.about-lead{left:654px;top:920px;width:430px;font-size:16px;line-height:19px;color:var(--ink)}
.about-body{left:654px;top:976px;width:435px;font-size:11px;line-height:18px;color:var(--text)}
.about-body p{margin-bottom:12px}
.about-pitch{left:654px;top:1139px;width:430px;font-size:16px;line-height:20px;color:var(--ink)}
.checks{left:654px;top:1198px;display:flex;gap:28px;font-size:12px;color:var(--ink)}
.checks svg{width:15px;height:15px;vertical-align:-3px;margin-right:7px}

/* why */
.why{left:0;top:1390px;width:1200px;height:520px;background:var(--blush)}
.why-title{left:0;top:1466px;width:1200px;text-align:center;font-size:28px;line-height:29px}
.feature{top:1598px;width:205px}
.feature-icon{width:64px;height:64px;border:1.5px solid var(--copper);border-radius:50%;display:flex;align-items:center;justify-content:center;background:var(--white)}
.feature-icon svg{width:34px;height:34px}
.feature h3{margin-top:16px;font-family:'Roboto',sans-serif;font-weight:500;font-size:15px;color:var(--copper)}
.feature p{margin-top:10px;font-size:11px;line-height:18px;color:var(--ink)}

/* services */
.svc-eyebrow{left:0;top:1998px;width:1200px;text-align:center;font-size:9px}
.svc-title{left:0;top:2022px;width:1200px;text-align:center;font-size:28px;line-height:29px;font-style:italic}
.card{top:2169px;width:310px;height:373px;background:var(--white);border-radius:0 0 40px 0;box-shadow:0 10px 28px rgba(0,0,0,.08)}
.card-photo{position:absolute;left:0;top:0;width:310px;height:167px}
.card-icon{position:absolute;left:33px;top:140px;width:62px;height:62px;border-radius:50%;background:var(--white);box-shadow:0 4px 12px rgba(0,0,0,.12);display:flex;align-items:center;justify-content:center}
.card-icon svg{width:30px;height:30px}
.card h3{position:absolute;left:34px;top:226px;font-size:14px;font-weight:500;color:var(--copper)}
.card p{position:absolute;left:34px;top:252px;width:250px;font-size:11px;line-height:18px;color:var(--muted)}
.card .btn{left:34px;top:358px;width:139px;height:39px}
.card.featured{background:var(--copper)}
.card.featured h3,.card.featured p{color:var(--white)}
.card.featured .btn{background:var(--navy)}

/* testimonial */
.testi-bg{left:0;top:2679px;width:1200px;height:498px;background:var(--blush)}
.testi-photo{left:0;top:2679px;width:640px;height:498px;border-top-left-radius:90px;background:linear-gradient(120deg,#dfe3e6 0%,#b9c3cb 40%,#8797a6 75%,#4f6274 100%)}
.testi-title{left:644px;top:2752px;font-size:28px;line-height:29px}
.avatar{left:644px;top:2868px;width:72px;height:72px;border-radius:50%;background:linear-gradient(135deg,#6c4a3e,#2e2624);border:3px solid var(--white)}
.testi-name{left:736px;top:2894px;font-size:18px;color:var(--ink);letter-spacing:.5px}
.stars{left:736px;top:2918px;color:var(--copper);font-size:12px;letter-spacing:2px}
.testi-quote{left:644px;top:2954px;width:375px;font-size:11px;line-height:17px;color:var(--ink)}
.arrows{left:644px;top:3032px;display:flex;align-items:center;gap:22px}

/* footer */
.footer{left:0;top:3177px;width:1200px;height:543px;background:var(--navy)}
.foot-head{font-family:'Montserrat',sans-serif;font-weight:700;color:var(--copper);font-size:13px;letter-spacing:.5px}
.contact-item{left:113px;display:flex;align-items:center;gap:12px;font-size:12px;line-height:17px;color:var(--white)}
.contact-item .ico{width:24px;height:24px;border:1px solid var(--copper);border-radius:50%;display:flex;align-items:center;justify-content:center;flex:none}
.contact-item svg{width:11px;height:11px;fill:var(--copper)}
.quick{left:417px;top:3400px;list-style:none;font-size:11px;color:var(--white)}
.quick li{height:33.5px;display:flex;align-items:center;gap:12px}
.quick li::before{content:"";width:4px;height:4px;border-radius:50%;background:var(--copper)}
.foot-rule{left:113px;top:3578px;width:460px;height:1px;background:rgba(255,255,255,.15)}
.copyright{left:113px;top:3601px;font-size:10px;line-height:16px;color:#cfd3da}
.social{top:3601px;width:32px;height:32px;border:1px solid rgba(255,255,255,.45);border-radius:50%}

/* contact form */
.form-card{left:644px;top:3136px;width:443px;height:491px;background:var(--copper);border-radius:60px 110px 0 0}
.form-title{left:702px;top:3192px;font-size:27px;color:var(--white)}
.form-desc{left:702px;top:3230px;width:320px;font-size:10.5px;line-height:16px;color:#fbeee9}
.field{left:702px;width:323px;border-bottom:1px solid rgba(255,255,255,.55);font-size:11px;color:var(--white);display:flex;justify-content:space-between;align-items:flex-start}
.field.soft{color:rgba(255,255,255,.7)}
.field .fi{width:20px;height:20px;border:1px solid rgba(255,255,255,.8);border-radius:50%;display:flex;align-items:center;justify-content:center}
.field .fi svg{width:10px;height:10px;fill:var(--white)}
.submit{left:702px;top:3526px;width:323px;height:38px;background:var(--navy);border-radius:0 20px 0 20px;display:flex;align-items:center;justify-content:center;gap:8px;color:var(--white);font-family:'Montserrat',sans-serif;font-weight:700;font-size:12px}
</style>
</head>
<body>

<!-- hero -->
<section class="abs hero" role="img" aria-label="Photo of a smiling accountant in glasses working at a laptop in a bright office"></section>
<div class="abs brand" style="left:113px;top:30px"><span class="brand-mark"></span><span>Meridian<br><span style="font-size:15px">Escrow Solutions</span></span></div>
<div class="abs hero-topbar">
  <span><svg viewBox="0 0 16 12"><path d="M0 0h16v12H0z M1 1l7 6 7-6" fill="none" stroke="#fff" stroke-width="1.5"/></svg>| Email: jcarver@meridianescrow.com</span>
  <span><svg viewBox="0 0 24 24"><path d="M6.6 10.8a15 15 0 006.6 6.6l2.2-2.2a1 1 0 011-.25 11.4 11.4 0 003.6.6 1 1 0 011 1V20a1 1 0 01-1 1A17 17 0 013 4a1 1 0 011-1h3.5a1 1 0 011 1c0 1.25.2 2.45.6 3.6a1 1 0 01-.25 1z"/></svg>| Call Us: 555-014-2087</span>
</div>
<nav>
  <span class="abs nav" style="left:799px">Home</span>
  <span class="abs nav" style="left:864px">About Us</span>
  <span class="abs nav" style="left:947px">Services</span>
  <span class="abs nav" style="left:1025px">Contact Us</span>
</nav>
<div class="abs eyebrow hero-eyebrow">Escrow Accounting Services</div>
<h1 class="abs heading hero-title" style="color:#fff">Your <span class="accent">Financial<br>Success,</span><br>Our Expertise</h1>
<p class="abs hero-copy">We offer a full suite of accounting services designed to streamline your financial operations and help you make informed decisions.</p>
<div class="abs dots"><span class="ring"></span><i></i><i></i><i></i><i style="opacity:.5"></i></div>

<!-- about -->
<div class="abs about-photo" role="img" aria-label="Photo of two smiling business professionals standing together"></div>
<div class="abs eyebrow about-eyebrow">About Us</div>
<h2 class="abs heading about-title">Meridian <span class="accent">Escrow</span><br>Solutions</h2>
<div class="divider" style="left:654px;top:875px;width:434px"><span style="left:7px"></span></div>
<p class="abs about-lead">Our Team Of <span class="accent">Experienced Professionals</span> Is The Ideal Solution For Your Needs.</p>
<div class="abs about-body">
  <p>Meridian Escrow Solutions has accounting experts who understand the title industry and the importance of compliance, security, and implementing precise escrow accounting procedures along with timely monthly reporting.</p>
  <p>Escrow accounting services are at the heart of what we do. Trust us to provide you with peace of mind. With Meridian Escrow Solutions, you can be confident that your escrow accounting will be secure, accurate, and in complete compliance with Underwriter Requirements and Best Practices.</p>
</div>
<p class="abs about-pitch">Put our knowledge and experience to work for you.<br>We want to help you achieve 100%</p>
<div class="abs checks">
  <span><svg viewBox="0 0 16 16"><circle cx="8" cy="8" r="7" fill="none" stroke="#c0725a" stroke-width="1.3"/><path d="M4.5 8.2l2.3 2.3 4.8-5" fill="none" stroke="#c0725a" stroke-width="1.5"/></svg>Compliance</span>
  <span><svg viewBox="0 0 16 16"><circle cx="8" cy="8" r="7" fill="none" stroke="#c0725a" stroke-width="1.3"/><path d="M4.5 8.2l2.3 2.3 4.8-5" fill="none" stroke="#c0725a" stroke-width="1.5"/></svg>Efficiency</span>
  <span><svg viewBox="0 0 16 16"><circle cx="8" cy="8" r="7" fill="none" stroke="#c0725a" stroke-width="1.3"/><path d="M4.5 8.2l2.3 2.3 4.8-5" fill="none" stroke="#c0725a" stroke-width="1.5"/></svg>Integrity</span>
</div>
<a class="btn" style="left:654px;top:1258px;width:139px;height:39px">Read More <svg viewBox="0 0 16 8"><path d="M0 4h14M11 1l3 3-3 3" fill="none" stroke="#fff" stroke-width="1.4"/></svg></a>

<!-- why choose -->
<section class="abs why"></section>
<h2 class="abs heading why-title">Why Choose <span class="accent">Meridian Escrow</span><br>Solutions</h2>
<div class="divider" style="left:349px;top:1544px;width:502px"><span></span></div>

<div class="abs feature" style="left:113px">
  <div class="feature-icon"><svg viewBox="0 0 34 34"><g fill="#363e4e"><circle cx="10" cy="14" r="3.5"/><circle cx="24" cy="14" r="3.5"/><circle cx="17" cy="16" r="4"/><path d="M4 27c0-4 3-7 6-7s4 1 4 1M30 27c0-4-3-7-6-7s-4 1-4 1M10 29c0-5 3-8 7-8s7 3 7 8z"/></g><g fill="#c0725a"><path d="M10 4l1 2h2l-1.6 1.3.6 2-2-1.2-2 1.2.6-2L7 6h2z"/><path d="M17 2l1 2h2l-1.6 1.3.6 2-2-1.2-2 1.2.6-2L14 4h2z"/><path d="M24 4l1 2h2l-1.6 1.3.6 2-2-1.2-2 1.2.6-2L21 6h2z"/></g></svg></div>
  <h3>Expertise You Can Trust</h3>
  <p>Daily two-way reconciliation is a Best Practice Standard. Let us create a customized package that ensures your compliance and protects your reporting from audit deficiencies.</p>
</div>
<div class="abs feature" style="left:373px">
  <div class="feature-icon"><svg viewBox="0 0 34 34"><circle cx="15" cy="12" r="6" fill="#363e4e"/><path d="M5 30c0-7 4-11 10-11s10 4 10 11z" fill="#363e4e"/><path d="M8 12a7 7 0 0114 0" fill="none" stroke="#c0725a" stroke-width="2"/><circle cx="26" cy="25" r="5" fill="#c0725a"/><circle cx="26" cy="25" r="2" fill="#fff"/></svg></div>
  <h3>Personalized Service</h3>
  <p>We perform reconciliations across all accounting software systems using secure protocols aligning with NTSA Best Practice - Pillar 3 standards.</p>
</div>
<div class="abs feature" style="left:633px">
  <div class="feature-icon"><svg viewBox="0 0 34 34"><g fill="#363e4e"><rect x="6" y="20" width="4" height="9"/><rect x="12" y="16" width="4" height="13"/><rect x="18" y="12" width="4" height="17"/><rect x="24" y="8" width="4" height="21"/><rect x="4" y="29" width="26" height="1.5"/></g><path d="M6 16l8-6 5 3 9-8" fill="none" stroke="#c0725a" stroke-width="1.8"/></svg></div>
  <h3>Comprehensive Solutions</h3>
  <p>Comprehensive daily and monthly reports will be delivered securely using SecureVault. These reports will include a detailed breakdown of items that may require your attention. We also manage the submission of reconciliations to underwriters.</p>
</div>
<div class="abs feature" style="left:893px">
  <div class="feature-icon"><svg viewBox="0 0 34 34"><circle cx="18" cy="10" r="7" fill="#c0725a"/><text x="18" y="13.5" font-size="9" text-anchor="middle" fill="#fff" font-family="Roboto, sans-serif">$</text><path d="M3 22h6l5 3h6a2 2 0 010 4h-7M9 29l10 1 11-6a2 2 0 00-2-3l-8 4" fill="none" stroke="#363e4e" stroke-width="2"/></svg></div>
  <h3>Commitment to Accuracy</h3>
  <p>Our affordable rates allow your company to significantly enhance efficiency with minimal investment and focus on what matters. Pricing is based on account activity volume, and we offer discounts for multiple accounts.</p>
</div>

<!-- services -->
<div class="abs eyebrow svc-eyebrow">Our Services</div>
<h2 class="abs heading svc-title">Your Trusted Partner In<br>Financial Excellence</h2>
<div class="divider" style="left:368px;top:2098px;width:464px"><span></span></div>

<article class="abs card" style="left:113px">
  <div class="card-photo" role="img" aria-label="Photo of colleagues reviewing financial charts on a laptop" style="background:linear-gradient(135deg,#c9d3dc,#6f8396 60%,#34475a)"></div>
  <div class="card-icon"><svg viewBox="0 0 30 30"><rect x="6" y="3" width="14" height="22" rx="2" fill="#363e4e"/><rect x="8.5" y="6" width="9" height="4" fill="#fff"/><g fill="#fff"><rect x="8.5" y="12" width="2.5" height="2.5"/><rect x="12" y="12" width="2.5" height="2.5"/><rect x="8.5" y="16" width="2.5" height="2.5"/><rect x="12" y="16" width="2.5" height="2.5"/></g><circle cx="22" cy="22" r="5.5" fill="#c0725a"/><text x="22" y="25" font-size="8" text-anchor="middle" fill="#fff" font-family="Roboto, sans-serif">$</text></svg></div>
  <h3>Escrow Reconciliation Service</h3>
  <p>Curabitur tristique risus sed nisi lobortis, a mollis tellus finibus. Nunc vulputate dui sed ligulagra vida, at pulvinar turpis mollis. Ut faucibus, mi eget finibus mattis.</p>
  <a class="btn">Read More <svg viewBox="0 0 16 8"><path d="M0 4h14M11 1l3 3-3 3" fill="none" stroke="#fff" stroke-width="1.4"/></svg></a>
</article>
<article class="abs card featured" style="left:445px">
  <div class="card-photo" role="img" aria-label="Photo of a calculator, glasses and paperwork on a desk" style="background:linear-gradient(135deg,#f0f0ef,#b8bcc0 55%,#5c636b)"></div>
  <div class="card-icon"><svg viewBox="0 0 30 30"><rect x="6" y="3" width="15" height="21" rx="1.5" fill="#363e4e"/><g stroke="#fff" stroke-width="1.5"><path d="M9 8h9M9 12h9M9 16h5"/></g><circle cx="21" cy="21" r="5" fill="#c0725a"/><path d="M18.8 21l1.6 1.6 3-3" fill="none" stroke="#fff" stroke-width="1.4"/></svg></div>
  <h3>NTSA Best Practice Certification</h3>
  <p>Curabitur tristique risus sed nisi lobortis, a mollis tellus finibus. Nunc vulputate dui sed ligulagra vida, at pulvinar turpis mollis. Ut faucibus, mi eget finibus mattis.</p>
  <a class="btn">Read More <svg viewBox="0 0 16 8"><path d="M0 4h14M11 1l3 3-3 3" fill="none" stroke="#fff" stroke-width="1.4"/></svg></a>
</article>
<article class="abs card" style="left:777px">
  <div class="card-photo" role="img" aria-label="Photo of a smiling support agent wearing a headset in an office" style="background:linear-gradient(135deg,#dfe2e4,#9aa5ae 55%,#3f4751)"></div>
  <div class="card-icon"><svg viewBox="0 0 30 30"><circle cx="15" cy="12" r="6" fill="#363e4e"/><path d="M5 28c0-6 4-9 10-9s10 3 10 9z" fill="#363e4e"/><path d="M8 13a7 7 0 0114 0" fill="none" stroke="#c0725a" stroke-width="2"/></svg></div>
  <h3>Data Call Services</h3>
  <p>Curabitur tristique risus sed nisi lobortis, a mollis tellus finibus. Nunc vulputate dui sed ligulagra vida, at pulvinar turpis mollis. Ut faucibus, mi eget finibus mattis.</p>
  <a class="btn">Read More <svg viewBox="0 0 16 8"><path d="M0 4h14M11 1l3 3-3 3" fill="none" stroke="#fff" stroke-width="1.4"/></svg></a>
</article>

<!-- testimonial -->
<section class="abs testi-bg"></section>
<div class="abs testi-photo" role="img" aria-label="Photo of a smiling man in glasses typing on a laptop"></div>
<h2 class="abs heading testi-title">See What <span class="accent">Our<br>Clients</span> Think</h2>
<div class="divider" style="left:644px;top:2827px;width:240px"><span></span></div>
<div class="abs avatar" role="img" aria-label="Client portrait"></div>
<div class="abs testi-name">Dana K.</div>
<div class="abs stars">★★★★★</div>
<p class="abs testi-quote">I recently engaged for our accounting needs, and the experience has been exceptional. From the initial consultation to the ongoing support, their team has demonstrated unparalleled professionalism and expertise.</p>
<div class="abs arrows">
  <svg width="36" height="8" viewBox="0 0 36 8"><path d="M36 4H2M5 1L2 4l3 3" fill="none" stroke="#c0725a" stroke-width="1.2"/></svg>
  <span style="position:relative;width:54px;height:30px;display:block">
    <span style="position:absolute;left:0;top:0;width:30px;height:30px;border-radius:50%;background:var(--copper)"></span>
    <svg style="position:absolute;left:14px;top:11px" width="40" height="8" viewBox="0 0 40 8"><path d="M0 4h38M35 1l3 3-3 3" fill="none" stroke="#363e4e" stroke-width="1.2"/></svg>
  </span>
</div>

<!-- footer -->
<footer class="abs footer"></footer>
<div class="abs brand" style="left:113px;top:3262px"><span class="brand-mark"></span><span>Meridian<br><span style="font-size:15px">Escrow Solutions</span></span></div>
<div class="abs foot-head" style="left:113px;top:3358px">CONTACT US</div>
<div class="abs contact-item" style="top:3402px"><span class="ico"><svg viewBox="0 0 24 24"><path d="M12 2a7 7 0 00-7 7c0 5 7 13 7 13s7-8 7-13a7 7 0 00-7-7zm0 9.5A2.5 2.5 0 1112 6a2.5 2.5 0 010 5.5z"/></svg></span><span>18 Harbor Crest Lane<br>Suite 400, Springfield 00000</span></div>
<div class="abs contact-item" style="top:3454px"><span class="ico"><svg viewBox="0 0 24 24"><path d="M2 5h20v14H2z M3 6l9 7 9-7" fill="none" stroke="#c0725a" stroke-width="2"/></svg></span><span>jcarver@meridianescrow.com</span></div>
<div class="abs contact-item" style="top:3494px"><span class="ico"><svg viewBox="0 0 24 24"><path d="M6.6 10.8a15 15 0 006.6 6.6l2.2-2.2a1 1 0 011-.25 11.4 11.4 0 003.6.6 1 1 0 011 1V20a1 1 0 01-1 1A17 17 0 013 4a1 1 0 011-1h3.5a1 1 0 011 1c0 1.25.2 2.45.6 3.6a1 1 0 01-.25 1z"/></svg></span><span>555-014-2087</span></div>
<div class="abs foot-head" style="left:417px;top:3358px">QUICK LINK</div>
<ul class="abs quick"><li>Home</li><li>About Us</li><li>Services</li><li>Contact Us</li></ul>
<div class="abs foot-rule"></div>
<p class="abs copyright">Copyright© 2024 <span class="accent">Meridian Escrow Solutions.</span><br>All Rights Reserved.</p>
<span class="abs social" style="left:417px"></span>
<span class="abs social" style="left:456px"></span>
<span class="abs social" style="left:497px"></span>

<!-- contact form -->
<section class="abs form-card"></section>
<h2 class="abs heading form-title">Get In Touch</h2>
<p class="abs form-desc">Contact us today for a consultation and embark on the journey to turn your construction dreams into a stunning reality.</p>
<div class="abs field" style="top:3294px;height:30px"><span>Name</span><span class="fi"><svg viewBox="0 0 24 24"><circle cx="12" cy="8" r="4"/><path d="M4 21c0-5 4-7 8-7s8 2 8 7z"/></svg></span></div>
<div class="abs field soft" style="top:3342px;height:31px"><span>Phone</span><span class="fi"><svg viewBox="0 0 24 24"><path d="M6.6 10.8a15 15 0 006.6 6.6l2.2-2.2a1 1 0 011-.25 11.4 11.4 0 003.6.6 1 1 0 011 1V20a1 1 0 01-1 1A17 17 0 013 4a1 1 0 011-1h3.5a1 1 0 011 1c0 1.25.2 2.45.6 3.6a1 1 0 01-.25 1z"/></svg></span></div>
<div class="abs field soft" style="top:3390px;height:30px"><span>Email</span><span class="fi"><svg viewBox="0 0 24 24"><path d="M2 5h20v14H2z M3 6l9 7 9-7" fill="none" stroke="#fff" stroke-width="2"/></svg></span></div>
<div class="abs field soft" style="top:3436px;height:60px"><span>Message</span><span class="fi"><svg viewBox="0 0 24 24"><path d="M3 17.2V21h3.8L18 9.8 14.2 6z"/></svg></span></div>
<a class="abs submit">Submit <svg width="16" height="8" viewBox="0 0 16 8"><path d="M0 4h14M11 1l3 3-3 3" fill="none" stroke="#fff" stroke-width="1.4"/></svg></a>

</body>
</html>
```